Business card por a urban DJ, up scale audience target

Need a sober design, modern, conservative colors but i can consider some options, y play rnb, hip hop, EDM and top40.

Business card for contact and personal info, double sided, use logo attrached please; im 42 so i need a card acording to my age an target audience.

Target Market(s)

Adult people, up scale audience

Industry/Entity Type

Music Download

Contact Information for Business Card

Cel (318) 5024471963 www.kelvarodun.com

Requirements
Must have
• open mind
Nice to have
• open mind
Should not have
• DJ

```html
<!DOCTYPE html>
<html lang="en">
<head>
<meta charset="UTF-8">
<title>Kelvaro Business Card</title>
<link href="https://fonts.googleapis.com/css2?family=Open+Sans:wght@400;600;800&display=swap" rel="stylesheet">
<style>
  :root {
    --canvas: #3a332f;
    --card: #0e0e0e;
    --card-edge: #1c1c1c;
    --ink: #ffffff;
    --ink-soft: #d9d9d9;
    --silver: #c9c9c9;
    --divider: #2a2a2a;
  }
  * { margin: 0; padding: 0; box-sizing: border-box; }
  html, body { width: 1200px; height: 900px; overflow: hidden; }
  body {
    background: var(--canvas);
    font-family: "Open Sans", Arial, sans-serif;
    display: flex;
    align-items: center;
    justify-content: center;
    gap: 40px;
  }
  .card {
    width: 525px;
    height: 300px;
    background: var(--card);
    border: 1px solid var(--card-edge);
    border-radius: 3px;
    position: relative;
    box-shadow: 0 10px 30px rgba(0,0,0,0.45);
    overflow: hidden;
  }
  /* back side */
  .card-back { display: flex; }
  .back-brand {
    width: 42%;
    flex: none;
    display: flex;
    align-items: flex-end;
    padding: 0 22px 70px 26px;
    border-right: 1px solid var(--divider);
  }
  .wordmark {
    font-weight: 800;
    color: var(--ink);
    letter-spacing: 1px;
    line-height: 1;
    display: flex;
    align-items: center;
    gap: 10px;
    white-space: nowrap;
  }
  .back-brand .wordmark { font-size: 25px; gap: 8px; }
  .back-brand .wordmark-square { width: 11px; height: 11px; }
  .wordmark-square {
    width: 14px;
    height: 14px;
    background: currentColor;
    flex: none;
  }
  .back-details {
    flex: 1;
    padding: 34px 0 0 28px;
    color: var(--ink-soft);
    font-size: 13px;
    line-height: 1.4;
  }
  .person-name { color: var(--ink); font-weight: 600; font-size: 16px; }
  .person-role { margin-bottom: 14px; }
  .address { margin-bottom: 12px; }
  .contact-list { list-style: none; }
  .contact-list li { display: flex; align-items: center; gap: 8px; }
  .contact-list svg { width: 11px; height: 11px; fill: var(--ink-soft); flex: none; }
  /* front side */
  .card-front {
    display: flex;
    align-items: center;
    justify-content: center;
  }
  .card-front .wordmark { font-size: 60px; color: var(--silver); gap: 16px; }
</style>
</head>
<body>
  <section class="card card-back">
    <div class="back-brand">
      <div class="wordmark"><span class="wordmark-square"></span>KELVARO</div>
    </div>
    <div class="back-details">
      <p class="person-name">Marcus Hale</p>
      <p class="person-role">Managing Director</p>
      <p class="address">4810 Harbor Lane, Suite 12<br>Riverton, 70112.</p>
      <ul class="contact-list">
        <li><svg viewBox="0 0 12 12"><path d="M2 1h2.5l1 3-1.5 1a7 7 0 0 0 3 3l1-1.5 3 1V10a1 1 0 0 1-1 1A9 9 0 0 1 1 2a1 1 0 0 1 1-1z"/></svg>(318) 5024471963</li>
        <li><svg viewBox="0 0 12 12"><path d="M1 2.5h10v7H1z M1.5 3l4.5 3.5L10.5 3" fill="none" stroke="#d9d9d9" stroke-width="1"/></svg>info@kelvarodun.com</li>
        <li><svg viewBox="0 0 12 12"><circle cx="6" cy="6" r="5"/></svg>www.kelvarodun.com</li>
      </ul>
    </div>
  </section>
  <section class="card card-front">
    <div class="wordmark"><span class="wordmark-square"></span>KELVARO</div>
  </section>
</body>
</html>
```